Images for my Portfolio

Hi,

I will use this theme

http://themes.morvenkallusta.com/html/veyra/light/index.html#work

and need 1 nice big image for each of my projects. So we have 9 images at the end but for mockup 1 image is enough for me to get an idea. The images should show different aspects of the site, so for example:

https://www.kornhainwerk.de/

There we have:
- Slideshow
- Configurator
- Cart etc.

Just have a look around and see whats special. Feel free in image-size and styling-elemets: frames, polaroid, 2D, 3D, mobile devices - do whatever you would do if you were me: a web-designer who wants to explain his last projects to the visitors.

Projects are:

https://www.kornhainwerk.de
http://dremmelhoff.de/
http://lorvix.de
http://www.kuechen-trinkgeraete-depot.de/
http://www.merowandruck.de/blog/info/haftbahnen/
http://pk-sprachmittlerin.de/de/
http://rmt-taxwert.de/
http://zutrittsbaender-markt7.de/
http://www.flink-u-blank.de/

This is not advertisement for my clients. I sell websites (!) so the purpose of the images is that my visitor can see what is possible if he hires me.

Thanks a lot

```html
<!DOCTYPE html>
<html lang="de">
<head>
<meta charset="utf-8">
<title>Braukranz – Startseite</title>
<link href="https://fonts.googleapis.com/css2?family=Open+Sans:wght@400;600;700&display=swap" rel="stylesheet">
<style>
  :root{
    --header-top:#2c2c2c;
    --header-bottom:#141414;
    --gold:#f0b400;
    --amber:#f7b81c;
    --white:#ffffff;
    --ink:#333333;
    --muted:#8a8a8a;
    --line:#e2e2e2;
    --footer:#262626;
    --stage:#1b1b1b;
  }
  *{box-sizing:border-box;margin:0;padding:0}
  html,body{width:1200px;height:668px;overflow:hidden;background:var(--stage);font-family:"Open Sans",Arial,sans-serif}
  .canvas{position:relative;width:1200px;height:668px;overflow:hidden}
  .panel{position:absolute;top:0;height:668px;overflow:hidden;background:var(--white)}
  .desktop{left:0;width:885px}
  .fullpage{left:885px;width:315px;border-left:1px solid #0d0d0d}
  .abs{position:absolute}

  /* ---------- desktop view ---------- */
  .site-header{position:absolute;left:0;top:0;width:100%;height:95px;background:linear-gradient(var(--header-top),var(--header-bottom))}
  .brand{position:absolute;display:flex;align-items:center;color:var(--white);font-weight:400}
  .brand-dot{border-radius:50%;background:var(--gold)}
  .desktop .brand{left:82px;top:38px;gap:10px;font-size:22px}
  .desktop .brand-dot{width:26px;height:26px}
  .service-bar{position:absolute;display:flex;align-items:flex-start;color:var(--white);font-weight:700;text-transform:uppercase;white-space:nowrap}
  .desktop .service-bar{left:315px;top:0;height:26px;font-size:8.5px}
  .delivery{display:flex;align-items:center;gap:5px;height:100%;padding-right:9px}
  .delivery em{font-style:normal;color:var(--gold)}
  .util-nav{display:flex;align-items:center;height:100%;background:var(--gold);border-radius:0 0 3px 3px}
  .desktop .util-nav{padding:0 10px;gap:16px}
  .util-nav .count{color:#6b4800}
  .cart{display:flex;align-items:center;gap:4px}
  .main-nav{position:absolute;display:flex;color:var(--white);font-weight:600;text-transform:uppercase;text-align:center;list-style:none}
  .main-nav li{border-left:1px solid #3e3e3e}
  .main-nav li:first-child{border-left:none}
  .desktop .main-nav{left:240px;top:52px;font-size:12.5px;line-height:14px}
  .desktop .main-nav li{padding:0 13px}
  .desktop .main-nav li.single{padding-top:7px}

  .hero{position:absolute;left:0;width:100%;background:radial-gradient(ellipse at 55% 40%,#a8692c 0%,#6d3e18 50%,#2e190a 100%)}
  .desktop .hero{top:95px;height:423px}
  .hero-visual{position:absolute;border-radius:24px 24px 0 0;background:linear-gradient(180deg,#f2ebde 0%,#efe6d6 16%,#e9a43a 28%,#c77914 72%,#8e5210 100%)}
  .desktop .hero-visual{left:360px;top:45px;width:460px;height:378px}
  .hero-copy{position:absolute;color:var(--white);text-align:center}
  .desktop .hero-copy{left:125px;top:145px;width:180px}
  .desktop .hero-copy h2{font-size:21px;font-weight:600;white-space:nowrap}
  .desktop .hero-copy p{margin-top:6px;font-size:16.5px;line-height:20px;font-weight:600;color:var(--amber);margin-left:0;width:190px}
  .btn{display:inline-flex;align-items:center;gap:6px;background:#1d1d1d;color:var(--white);font-weight:600;border-radius:3px;white-space:nowrap}
  .desktop .btn{font-size:12px;padding:7px 12px;margin-top:14px}
  .desktop .arrow-prev{left:72px;top:200px}
  .desktop .arrow-next{left:686px;top:200px}

  .intro{position:absolute;left:0;width:100%;text-align:center}
  .desktop .intro{top:518px;height:150px}
  .desktop .intro h1{margin-top:32px;font-size:22px;font-weight:400;color:var(--ink);white-space:nowrap}
  .intro h1 em{font-style:normal;color:var(--gold)}
  .lede{display:flex;align-items:center;justify-content:center;color:var(--muted);white-space:nowrap}
  .lede i{display:block;height:1px;background:var(--line)}
  .lede a{color:var(--gold);text-decoration:none}
  .desktop .lede{gap:12px;margin-top:10px;font-size:12.5px}
  .desktop .lede i{width:150px}
  .steps{display:flex;justify-content:center}
  .desktop .steps{gap:40px;margin-top:16px}
  .step-img{border-radius:50%;border:3px solid #ededed;margin:0 auto}
  .desktop .step-img{width:62px;height:62px}

  /* ---------- full page view ---------- */
  .fullpage .site-header{height:35px}
  .fullpage .brand{left:16px;top:12px;gap:4px;font-size:9px}
  .fullpage .brand-dot{width:10px;height:10px}
  .fullpage .service-bar{left:118px;top:0;height:8px;font-size:3.5px}
  .fullpage .delivery{padding-right:3px;gap:2px}
  .fullpage .util-nav{padding:0 4px;gap:6px}
  .fullpage .main-nav{left:88px;top:18px;font-size:4.6px;line-height:5.4px}
  .fullpage .main-nav li{padding:0 5px}
  .fullpage .main-nav li.single{padding-top:2.7px}

  .fullpage .hero{top:35px;height:157px}
  .fullpage .hero-visual{left:125px;top:16px;width:160px;height:141px;border-radius:10px 10px 0 0}
  .fullpage .hero-copy{left:38px;top:54px;width:60px}
  .fullpage .hero-copy h2{font-size:7.5px;font-weight:600;white-space:nowrap}
  .fullpage .hero-copy p{margin-top:2px;font-size:5.6px;line-height:6.6px;font-weight:600;color:var(--amber)}
  .fullpage .btn{font-size:4.5px;padding:2px 5px;margin-top:6px;gap:3px}
  .fullpage .arrow-prev{left:16px;top:74px}
  .fullpage .arrow-next{left:245px;top:74px}

  .fullpage .intro{top:192px;height:140px;background:#fafafa}
  .fullpage .intro h1{margin-top:14px;font-size:8.4px;font-weight:400;color:var(--ink);white-space:nowrap}
  .fullpage .lede{gap:5px;margin-top:5px;font-size:5px}
  .fullpage .lede i{width:45px}
  .fullpage .steps{gap:12px;margin-top:9px}
  .fullpage .step{width:38px;font-size:3.8px;line-height:4.5px;color:var(--muted)}
  .fullpage .step-img{width:36px;height:36px;border-width:1.5px;margin-bottom:3px}
  .fullpage .intro .btn{margin-top:7px}

  .block{position:absolute;left:0;width:100%;text-align:center}
  .block h3{display:flex;align-items:center;justify-content:center;gap:8px;font-size:6.5px;font-weight:600;color:var(--ink)}
  .block h3 i{display:block;width:110px;height:1px;background:var(--line)}
  .block .cols{display:grid;grid-template-columns:repeat(4,60px);justify-content:center;margin-top:10px}
  .tile-img{width:44px;height:44px;border-radius:50%;margin:0 auto 5px}
  .tile-title{font-size:4.6px;font-weight:600;color:var(--ink)}
  .tile-text{margin:3px auto 0;width:52px;font-size:3.6px;line-height:5px;color:var(--muted)}
  .products{top:338px}
  .promise{top:486px}
  .promise .tile-img{width:42px;height:42px}

  .site-footer{position:absolute;left:0;top:605px;width:100%;height:63px;background:var(--footer);display:grid;grid-template-columns:repeat(5,1fr);padding:8px 12px 0;gap:6px}
  .site-footer h4{font-size:3.8px;font-weight:700;color:var(--gold);text-transform:uppercase;margin-bottom:3px}
  .site-footer p{font-size:3.4px;line-height:5px;color:#9a9a9a}
  .social{display:flex;gap:2px;margin-top:1px}
  .social span{width:6px;height:6px;border-radius:50%;background:#9a9a9a}
  .badge{width:26px;height:9px;background:#d8d8d8;margin-top:3px}
  .news-field{width:44px;height:6px;background:#ffffff;margin-bottom:3px}
  .news-btn{width:24px;height:6px;background:var(--gold);margin-top:3px}
</style>
</head>
<body>
<div class="canvas">

  <!-- Desktop view -->
  <div class="panel desktop">
    <header class="site-header">
      <div class="brand"><span class="brand-dot"></span>Braukranz</div>
      <div class="service-bar">
        <div class="delivery">
          <svg width="20" height="12" viewBox="0 0 22 14"><rect x="0" y="2" width="13" height="8" fill="#fff"/><path d="M13 4h5l3 3v3h-8z" fill="#fff"/><circle cx="5" cy="11.5" r="2" fill="#fff" stroke="#222"/><circle cx="17" cy="11.5" r="2" fill="#fff" stroke="#222"/></svg>
          Lieferung <em>innerhalb 1 Woche</em>
        </div>
        <nav class="util-nav">
          <span>Nachbestellen</span><span>Über uns</span><span>Login</span>
          <span class="cart"><svg width="12" height="10" viewBox="0 0 12 10"><path d="M0 1h2l2 6h6l2-5H3" fill="none" stroke="#fff" stroke-width="1.4"/></svg>Warenkorb <span class="count">(0)</span></span>
        </nav>
      </div>
      <ul class="main-nav">
        <li>Bier<br>konfigurieren</li>
        <li>Unsere<br>Besten &amp; mehr</li>
        <li>Als<br>Geschenk</li>
        <li>Für<br>Events</li>
        <li class="single">Fragen</li>
      </ul>
    </header>

    <section class="hero">
      <div class="hero-visual" role="img" aria-label="Foto zweier gefüllter Biergläser mit Schaumkrone vor warmem braunen Hintergrund"></div>
      <div class="hero-copy">
        <h2>Unsere Besten.</h2>
        <p>Die deluxe Biere und die Probiersets von Braukranz.</p>
        <span class="btn">Jetzt probieren <svg width="7" height="10" viewBox="0 0 7 10"><path d="M1 1l4 4-4 4" stroke="#f0b400" stroke-width="2" fill="none"/></svg></span>
      </div>
      <svg class="abs arrow-prev" width="16" height="26" viewBox="0 0 16 26"><path d="M13 2L3 13l10 11" stroke="#fff" stroke-width="4" fill="none"/></svg>
      <svg class="abs arrow-next" width="16" height="26" viewBox="0 0 16 26"><path d="M3 2l10 11L3 24" stroke="#fff" stroke-width="4" fill="none"/></svg>
    </section>

    <section class="intro">
      <h1>Für den besonderen Moment das besondere Bier. <em>Deins.</em></h1>
      <div class="lede"><i></i><span>Bier selbst konfigurieren: so geht's <a href="#">(zum Film)</a></span><i></i></div>
      <div class="steps">
        <div class="step-img" role="img" aria-label="Bierglas" style="background:radial-gradient(circle,#e3a02a,#f1efe9)"></div>
        <div class="step-img" role="img" aria-label="Hopfendolden" style="background:radial-gradient(circle,#8dbf3a,#e9f0dc)"></div>
        <div class="step-img" role="img" aria-label="Messskala" style="background:radial-gradient(circle,#ffffff,#bdbdbd)"></div>
        <div class="step-img" role="img" aria-label="Perlendes Bier" style="background:radial-gradient(circle,#f6c552,#e39c16)"></div>
        <div class="step-img" style="background:linear-gradient(90deg,#f7f7f7 50%,#f6b521 50%)"></div>
      </div>
    </section>
  </div>

  <!-- Full page view -->
  <div class="panel fullpage">
    <header class="site-header">
      <div class="brand"><span class="brand-dot"></span>Braukranz</div>
      <div class="service-bar">
        <div class="delivery">Lieferung <em>innerhalb 1 Woche</em></div>
        <nav class="util-nav"><span>Nachbestellen</span><span>Über uns</span><span>Login</span><span>Warenkorb <span class="count">(0)</span></span></nav>
      </div>
      <ul class="main-nav">
        <li>Bier<br>konfigurieren</li>
        <li>Unsere<br>Besten &amp; mehr</li>
        <li>Als<br>Geschenk</li>
        <li>Für<br>Events</li>
        <li class="single">Fragen</li>
      </ul>
    </header>

    <section class="hero">
      <div class="hero-visual" role="img" aria-label="Foto zweier gefüllter Biergläser mit Schaumkrone"></div>
      <div class="hero-copy">
        <h2>Unsere Besten.</h2>
        <p>Die deluxe Biere und die Probiersets von Braukranz.</p>
        <span class="btn">Jetzt probieren <svg width="3" height="5" viewBox="0 0 7 10"><path d="M1 1l4 4-4 4" stroke="#f0b400" stroke-width="2" fill="none"/></svg></span>
      </div>
      <svg class="abs arrow-prev" width="6" height="10" viewBox="0 0 16 26"><path d="M13 2L3 13l10 11" stroke="#fff" stroke-width="4" fill="none"/></svg>
      <svg class="abs arrow-next" width="6" height="10" viewBox="0 0 16 26"><path d="M3 2l10 11L3 24" stroke="#fff" stroke-width="4" fill="none"/></svg>
    </section>

    <section class="intro">
      <h1>Für den besonderen Moment das besondere Bier. <em>Deins.</em></h1>
      <div class="lede"><i></i><span>Bier selbst konfigurieren: so geht's <a href="#">(zum Film)</a></span><i></i></div>
      <div class="steps">
        <div class="step"><div class="step-img" role="img" aria-label="Bierglas" style="background:radial-gradient(circle,#e3a02a,#f1efe9)"></div>Biertyp wählen</div>
        <div class="step"><div class="step-img" role="img" aria-label="Hopfendolden" style="background:radial-gradient(circle,#8dbf3a,#e9f0dc)"></div>Hopfenintensität einstellen</div>
        <div class="step"><div class="step-img" role="img" aria-label="Messskala" style="background:radial-gradient(circle,#ffffff,#bdbdbd)"></div>Alkoholgehalt festlegen</div>
        <div class="step"><div class="step-img" role="img" aria-label="Perlendes Bier" style="background:radial-gradient(circle,#f6c552,#e39c16)"></div>Spritzigkeit bestimmen</div>
        <div class="step"><div class="step-img" style="background:linear-gradient(90deg,#f7f7f7 50%,#f6b521 50%)"></div>Farbintensität vorgeben</div>
      </div>
      <span class="btn">Jetzt konfigurieren <svg width="3" height="5" viewBox="0 0 7 10"><path d="M1 1l4 4-4 4" stroke="#f0b400" stroke-width="2" fill="none"/></svg></span>
    </section>

    <section class="block products">
      <h3><i></i>Produkte<i></i></h3>
      <div class="cols">
        <div><div class="tile-img" role="img" aria-label="Bierflasche und Glas" style="background:radial-gradient(circle,#c58a2a,#2a2a2a)"></div><div class="tile-title">Bier konfigurieren</div><p class="tile-text">Dein Bier nach eigenem Geschmack gebraut.</p></div>
        <div><div class="tile-img" role="img" aria-label="Probierset mit Gläsern" style="background:radial-gradient(circle,#e9a43a,#eeeeee)"></div><div class="tile-title">Unsere Besten &amp; Mehr</div><p class="tile-text">Ausgewählte Biere und Probiersets zum Entdecken.</p></div>
        <div><div class="tile-img" role="img" aria-label="Geschenkbox mit roter Schleife" style="background:radial-gradient(circle,#b01e1e,#1e1e1e)"></div><div class="tile-title">Als Geschenk</div><p class="tile-text">Ein persönliches Bier als besondere Überraschung.</p></div>
        <div><div class="tile-img" role="img" aria-label="Feuerwerk und Bierglas" style="background:radial-gradient(circle,#3a4f8a,#101830)"></div><div class="tile-title">Für Events</div><p class="tile-text">Eigenes Bier für Feiern und Firmenanlässe.</p></div>
      </div>
    </section>

    <section class="block promise">
      <h3><i></i>Unser Versprechen<i></i></h3>
      <div class="cols">
        <div><div class="tile-img" role="img" aria-label="Brauzutaten" style="background:radial-gradient(circle,#9a9a9a,#4a4a4a)"></div><div class="tile-title">Individuell und rein</div><p class="tile-text">Nur beste Zutaten nach deinen Wünschen.</p></div>
        <div><div class="tile-img" role="img" aria-label="Reifendes Bier" style="background:radial-gradient(circle,#8a8a8a,#3a3a3a)"></div><div class="tile-title">Natürlich belassen</div><p class="tile-text">Ohne Zusätze, schonend gereift und frisch.</p></div>
        <div><div class="tile-img" role="img" aria-label="Braukessel" style="background:radial-gradient(circle,#a0a0a0,#505050)"></div><div class="tile-title">Mit Liebe gebraut</div><p class="tile-text">Handwerk mit Zeit und viel Sorgfalt.</p></div>
        <div><div class="tile-img" role="img" aria-label="Kalender für Lieferung" style="background:radial-gradient(circle,#f2f2f2,#7a7a7a)"></div><div class="tile-title">Frisch geliefert</div><p class="tile-text">In wenigen Tagen direkt zu dir.</p></div>
      </div>
    </section>

    <footer class="site-footer">
      <div><h4>Produkte</h4><p>Bier konfigurieren<br>Unsere Besten<br>Als Geschenk<br>Für Events</p></div>
      <div><h4>Service</h4><p>Fragen<br>Versand<br>Nachbestellen</p></div>
      <div><h4>Rechtliches</h4><p>Impressum<br>Datenschutz<br>AGB</p></div>
      <div><h4>Bleib in Kontakt</h4><div class="social"><span></span><span></span><span></span><span></span></div><div class="badge"></div></div>
      <div><h4>Newsletter</h4><div class="news-field"></div><p>Neuigkeiten direkt ins Postfach.</p><div class="news-btn"></div></div>
    </footer>
  </div>

</div>
</body>
</html>
```